ALL TEXT Social Media Graphics

We are looking for a series of social media graphics for Instagram (new size: 4:5 (1080 x 1350 pixels) ratio that are ALL TEXT. We want the following quotes below on each graphic; one quote per graphic. AND, In very small letters at the bottom of each graphic, add @PaulaWrenLive
The look and feel of these graphics should be complimentary to the color palette attached below; but keep them simple. But the design is up to you; at the end of this document, I provided various samples of all text graphics that I like as examples.
The Quotes are in the attached WORD document
women trying to lose weight

```html
<!DOCTYPE html>
<html lang="en">
<head>
<meta charset="utf-8">
<title>Summer Slimdown Post</title>
<link href="https://fonts.googleapis.com/css2?family=Montserrat:wght@800&family=Roboto:wght@500&display=swap" rel="stylesheet">
<style>
  :root {
    --pink: #ec3f8c;
    --teal: #2f5560;
    --berry: #a3215a;
    --blush-end: #fbc2d5;
    --white: #ffffff;
  }
  html, body {
    margin: 0;
    padding: 0;
    width: 960px;
    height: 1200px;
    overflow: hidden;
  }
  .post {
    position: relative;
    width: 960px;
    height: 1200px;
    background: linear-gradient(to bottom, var(--white) 0%, var(--white) 63%, #fde6ee 80%, var(--blush-end) 100%);
    font-family: "Montserrat", Arial, sans-serif;
  }
  .headline, .pitch, .cta, .handle {
    position: absolute;
    left: 98px;
    margin: 0;
    white-space: nowrap;
  }
  .headline {
    top: 66px;
    font-weight: 800;
    font-size: 80px;
    line-height: 101px;
    letter-spacing: -1px;
    color: var(--pink);
  }
  .pitch {
    top: 512px;
    font-weight: 800;
    font-size: 72px;
    line-height: 93px;
    letter-spacing: -1px;
    color: var(--teal);
  }
  .cta {
    top: 922px;
    font-family: "Roboto", Arial, sans-serif;
    font-weight: 500;
    font-size: 68px;
    line-height: 80px;
    color: var(--berry);
  }
  .handle {
    top: 1066px;
    font-family: "Roboto", Arial, sans-serif;
    font-weight: 500;
    font-size: 44px;
    line-height: 52px;
    color: var(--teal);
  }
</style>
</head>
<body>
  <main class="post">
    <h1 class="headline">You’ve got 8<br>weeks and the<br>perfect plan to<br>drop 30 pounds.</h1>
    <p class="pitch">Let’s get snatched<br>this summer with the<br>Sunny Season<br>Slimdown.</p>
    <p class="cta">Comment SUMMER!</p>
    <p class="handle">@PaulaWrenLive</p>
  </main>
</body>
</html>
```